Letter Head, for use on daily correspondence with other companies

Hi

I want a professional Letter head, That my company can use to corresponded with other companies we do business with on a daily basis.

I want this done as soon as possible as this is peak session for us.

I have attached the company logo so please be creative and professional.
Kind regards

Marcus

Target Market(s)

All Audience searching for tickets, people in the entertainment world

Industry/Entity Type

Entertainment Industry

Font styles to use
Serif
Sans Serif
Decorative
Script

Requirements
Must have
• Very professional image.
• I will know want i want when i see it
• so please do your utmost in your professional standards
• Address of the company 24 hollin lane, telephone number 0207 562 3198
• Vat number: 487 2915 06.
• This letter head my be able to acomodate usage for directors & CEO as well as managers and employess
Nice to have
• A great professional image
Should not have
• Be creative please

```html
<!DOCTYPE html>
<html lang="en">
<head>
<meta charset="utf-8">
<title>Lumora Tickets Letterhead</title>
<link href="https://fonts.googleapis.com/css2?family=Questrial&display=swap" rel="stylesheet">
<style>
  :root {
    --backdrop: #2b2b2b;
    --paper: #f4f4f4;
    --brand-red: #e8141b;
    --rule-grey: #a9a9a9;
    --ink: #444444;
  }
  * { margin: 0; padding: 0; box-sizing: border-box; }
  html, body { width: 1200px; height: 900px; overflow: hidden; }
  body {
    background: var(--backdrop);
    font-family: "Questrial", "Century Gothic", sans-serif;
    position: relative;
  }
  .sheet {
    position: absolute;
    top: 91px;
    width: 507px;
    height: 716px;
    background: var(--paper);
    box-shadow: 0 4px 14px rgba(0,0,0,0.45);
  }
  .sheet--classic { left: 72px; }
  .sheet--banded { left: 626px; }

  .top-band { position: absolute; top: 0; left: 0; right: 0; height: 9px; }
  .top-band__red { position: absolute; left: 0; top: 0; width: 331px; height: 9px; background: var(--brand-red); }
  .top-band__grey { position: absolute; left: 334px; right: 0; top: 0; height: 9px; background: var(--rule-grey); }

  .brand {
    position: absolute;
    left: 38px;
    top: 42px;
    color: var(--brand-red);
    font-weight: 400;
    line-height: 1;
  }
  .brand__name { display: block; font-size: 40px; letter-spacing: -0.5px; }
  .brand__sub { display: block; font-size: 7px; letter-spacing: 3px; text-align: right; margin-top: 1px; }

  .contact {
    position: absolute;
    left: 380px;
    top: 42px;
    list-style: none;
    font-size: 7.4px;
    color: var(--ink);
    line-height: 9px;
  }
  .contact__item { display: flex; align-items: center; gap: 4px; }
  .contact__icon { width: 7px; height: 7px; flex: none; }

  .footer {
    position: absolute;
    left: 38px;
    right: 38px;
    top: 691px;
    display: flex;
    justify-content: space-between;
    font-size: 7.4px;
    color: var(--ink);
  }
  .footer-rule {
    position: absolute;
    left: 38px;
    right: 38px;
    top: 683px;
    height: 1px;
    background: #777;
  }
  .bottom-band { position: absolute; left: 0; right: 0; bottom: 0; height: 9px; background: var(--brand-red); }
</style>
</head>
<body>

<svg width="0" height="0" style="position:absolute">
  <defs>
    <symbol id="icon-phone" viewBox="0 0 8 8">
      <rect width="8" height="8" rx="1" fill="#e8141b"/>
      <path d="M2.3 1.6 L3.3 2.6 L2.8 3.2 Q3.5 4.6 4.8 5.2 L5.4 4.7 L6.4 5.7 L5.6 6.5 Q2.2 5.8 1.5 2.4 Z" fill="#fff"/>
    </symbol>
    <symbol id="icon-square" viewBox="0 0 8 8">
      <rect width="8" height="8" rx="1" fill="#e8141b"/>
    </symbol>
    <symbol id="icon-mail" viewBox="0 0 8 8">
      <rect width="8" height="8" rx="1" fill="#e8141b"/>
      <rect x="1.6" y="2.4" width="4.8" height="3.2" fill="none" stroke="#fff" stroke-width="0.7"/>
      <path d="M1.6 2.4 L4 4.3 L6.4 2.4" fill="none" stroke="#fff" stroke-width="0.7"/>
    </symbol>
    <symbol id="icon-web" viewBox="0 0 8 8">
      <rect width="8" height="8" rx="1" fill="#e8141b"/>
      <circle cx="4" cy="4" r="2.4" fill="none" stroke="#fff" stroke-width="0.7"/>
      <path d="M1.6 4 H6.4" stroke="#fff" stroke-width="0.6"/>
    </symbol>
  </defs>
</svg>

<section class="sheet sheet--classic">
  <div class="top-band"><span class="top-band__red"></span><span class="top-band__grey"></span></div>
  <div class="brand"><span class="brand__name">lumora</span><span class="brand__sub">TICKETS</span></div>
  <ul class="contact">
    <li class="contact__item"><svg class="contact__icon"><use href="#icon-phone"/></svg>0207 562 3198</li>
    <li class="contact__item"><svg class="contact__icon"><use href="#icon-square"/></svg>lumoratickets</li>
    <li class="contact__item"><svg class="contact__icon"><use href="#icon-square"/></svg>@lumoratickets</li>
    <li class="contact__item"><svg class="contact__icon"><use href="#icon-mail"/></svg>info@lumoratickets.co.uk</li>
    <li class="contact__item"><svg class="contact__icon"><use href="#icon-web"/></svg>www.lumoratickets.co.uk</li>
  </ul>
  <div class="footer-rule"></div>
  <div class="footer"><span>Address: 24 Hollin Lane, N4 2QS</span><span>Vat number: 487 2915 06</span></div>
</section>

<section class="sheet sheet--banded">
  <div class="brand"><span class="brand__name">lumora</span><span class="brand__sub">TICKETS</span></div>
  <ul class="contact">
    <li class="contact__item"><svg class="contact__icon"><use href="#icon-phone"/></svg>0207 562 3198</li>
    <li class="contact__item"><svg class="contact__icon"><use href="#icon-square"/></svg>lumoratickets</li>
    <li class="contact__item"><svg class="contact__icon"><use href="#icon-square"/></svg>@lumoratickets</li>
    <li class="contact__item"><svg class="contact__icon"><use href="#icon-mail"/></svg>info@lumoratickets.co.uk</li>
    <li class="contact__item"><svg class="contact__icon"><use href="#icon-web"/></svg>www.lumoratickets.co.uk</li>
  </ul>
  <div class="footer"><span>Address: 24 Hollin Lane, N4 2QS</span><span>Vat number: 487 2915 06</span></div>
  <div class="bottom-band"></div>
</section>

</body>
</html>
```